World Wide Safety Management Product

Hi folks,
We need a website designed for a new product we are launching.

This product is to do with remote Health and Safety Management of people. Combining a wearable device, mobile app and a Portal our Product.

The Product is called 'MyTrekko.Globe' - as it's global and individual. (Trekko are the guides that help & assist you climb Everest)

I've put an initial brief design up to share more of the story with you - http://guardpal.examplehost.net
(I'm not particularly attached to anything on this design - it was something I needed to put together overnight)

We are a software development house and can take your design (in HTML cutup) and work with it - I do need a good creative design though, that will be easy to incorporate into web pages.

For the Initial Design - the landing page will be fine.

For the final design - ideally I'd like the other pages included.

Thank you very much designers unleash your creativity :)

Dave.
Updates

Target Market(s)

Male - 35-60 & females 35-60 working in distributed, decentralised roles for remote companies.

Industry/Entity Type

Media

Logo Text

A friend for life.

Coding

Coded - Design and coding required

Number of Pages Required

4 page

Font styles to use
Other font styles liked:
• 'Open Sans', Arial, Helvetica, sans-serif

Requirements
Must have
• What I'm looking for:
• - ultimate delivery in HTML5/CSS3 - Twitter bootstrap compliant.
• - I need someone who can design + take it through to HTML cutup.
• - creative, I dont want 'more of the same'
• - tells a story simplistically.
Nice to have
• - good use of imagery.
• - good use of white space (sometimes less is best)
Should not have
• Doctors & Nurses running around in imagery.
• We are not a medical provider & we do have plans in the future in this space, but not initially. Focus on the guided safety aspect.

```html
<!DOCTYPE html>
<html lang="en">
<head>
<meta charset="utf-8">
<title>MyTrekko.Globe – Safety management for smart wearables</title>
<link href="https://fonts.googleapis.com/css2?family=Roboto:wght@300;400;500;700&display=swap" rel="stylesheet">
<style>
  :root {
    --teal: #14a99b;
    --teal-bright: #17bfbf;
    --ink: #333538;
    --text: #555759;
    --muted-btn: #5b5d66;
    --hero-sky: #b6cce6;
    --panel: #f4f4f4;
    --footer: #3a3b3c;
    --white: #ffffff;
  }
  * { box-sizing: border-box; margin: 0; padding: 0; }
  html, body { width: 1200px; height: 1182px; overflow: hidden; }
  body {
    position: relative;
    font-family: 'Roboto', sans-serif;
    background: var(--white);
    color: var(--text);
  }
  a { color: inherit; text-decoration: none; }

  /* Header */
  .site-header { position: absolute; left: 0; top: 0; width: 1200px; height: 92px; background: var(--white); }
  .brand { position: absolute; left: 74px; top: 30px; display: flex; align-items: center; gap: 8px; }
  .brand-mark { width: 22px; height: 22px; border-radius: 50%; background: var(--teal); }
  .brand-name { font-size: 17px; font-weight: 500; color: var(--ink); }
  .main-nav { position: absolute; top: 42px; left: 431px; display: flex; gap: 0; font-size: 16px; color: var(--ink); }
  .main-nav a { margin-right: 31px; }
  .main-nav a.is-active { color: var(--teal); }
  .btn { position: absolute; top: 32px; height: 30px; border-radius: 15px; color: var(--white);
         font-size: 13px; text-transform: uppercase; display: flex; align-items: center; justify-content: center; }
  .btn-login { left: 937px; width: 76px; background: var(--teal-bright); }
  .btn-register { left: 1023px; width: 103px; background: var(--muted-btn); }

  /* Hero */
  .hero { position: absolute; left: 0; top: 92px; width: 1200px; height: 528px; background: var(--hero-sky); overflow: hidden; }
  .hero-visual { position: absolute; right: 0; top: 0; width: 560px; height: 528px;
    background: linear-gradient(90deg, rgba(182,204,230,0) 0%, #d7e3f0 40%, #e8eef5 70%, #c9b7ad 100%); }
  .hero-title { position: absolute; left: 94px; top: 140px; font-size: 42px; font-weight: 400; color: var(--ink); letter-spacing: -0.3px; }
  .hero-title strong { font-weight: 700; }
  .hero-sub { position: absolute; left: 94px; top: 202px; width: 680px; font-size: 22px; font-weight: 300; line-height: 28px; color: var(--white); }
  .hero-dots { position: absolute; left: 94px; top: 281px; display: flex; gap: 5px; }
  .hero-dots span { width: 12px; height: 12px; border-radius: 50%; background: var(--white); }
  .hero-dots span.is-active { background: #4a4c50; }

  /* Features card */
  .features { position: absolute; left: 74px; top: 510px; width: 1052px; height: 210px; background: #fcfcfc; }
  .features::after { content: ""; position: absolute; left: 30px; right: 30px; bottom: -8px; height: 8px;
    background: radial-gradient(ellipse at top, rgba(0,0,0,0.22), rgba(0,0,0,0) 70%); }
  .section-title { font-size: 26px; font-weight: 400; color: var(--ink); text-transform: uppercase; }
  .features .section-title { position: absolute; left: 29px; top: 26px; }
  .features-sub { position: absolute; left: 29px; top: 73px; font-size: 17.5px; color: var(--teal); text-transform: uppercase; }
  .features-copy { position: absolute; left: 31px; top: 100px; width: 720px; font-size: 13.5px; line-height: 19.5px; }
  .read-more { font-size: 13.5px; font-weight: 500; color: var(--teal); text-transform: uppercase; }
  .features .read-more { position: absolute; left: 31px; top: 167px; }
  .features-visual { position: absolute; left: 752px; top: 21px; width: 254px; height: 175px;
    background: radial-gradient(ellipse at center, #d9e6f4 0%, #eef2f6 55%, #fcfcfc 80%); }

  /* How it works */
  .how { position: absolute; left: 74px; top: 770px; width: 790px; }
  .how .section-title { position: absolute; left: 0; top: 0; }
  .step { position: absolute; top: 52px; width: 229px; }
  .step svg { display: block; height: 72px; }
  .step-title { margin-top: 22px; font-size: 16.5px; font-weight: 500; color: var(--teal); text-transform: uppercase; letter-spacing: 0.3px; }
  .step-copy { margin-top: 12px; font-size: 13.5px; line-height: 20.3px; text-align: justify; }
  .step-wear { left: 1px; }
  .step-mobile { left: 270px; }
  .step-control { left: 541px; }

  /* Blog */
  .blog { position: absolute; left: 884px; top: 780px; width: 242px; height: 260px; background: var(--panel); padding: 24px 25px; }
  .blog .section-title { font-size: 21px; }
  .blog-author { margin-top: 16px; display: flex; align-items: center; gap: 13px; }
  .avatar { width: 58px; height: 58px; border-radius: 50%; background: linear-gradient(135deg, #9fb7c9, #d1bfae); border: 2px solid var(--white); }
  .posted { font-size: 13px; color: var(--teal); }
  .author-name { font-size: 16px; color: var(--ink); margin-top: 2px; }
  .blog-copy { margin-top: 20px; font-size: 13.5px; line-height: 20.3px; text-align: justify; }
  .blog .read-more { display: block; margin-top: 15px; }

  /* Footer */
  .site-footer { position: absolute; left: 0; top: 1083px; width: 1200px; height: 99px; background: var(--footer); color: var(--white); }
  .footer-links { position: absolute; left: 77px; top: 32px; font-size: 14.5px; }
  .footer-links span { margin: 0 8px; }
  .copyright { position: absolute; left: 77px; top: 56px; font-size: 13.5px; }
  .copyright a { color: var(--teal-bright); }
  .social { position: absolute; left: 993px; top: 32px; display: flex; gap: 8px; }
  .social a { width: 38px; height: 38px; border-radius: 50%; }
  .social .s-one { background: #2f6fb5; }
  .social .s-two { background: #2aa3dd; }
  .social .s-three { background: #f4a02a; }
</style>
</head>
<body>
  <header class="site-header">
    <a class="brand" href="#"><span class="brand-mark"></span><span class="brand-name">mytrekko.globe</span></a>
    <nav class="main-nav">
      <a class="is-active" href="#">Home</a>
      <a href="#">Features</a>
      <a href="#">How it works</a>
      <a href="#">Blog</a>
      <a href="#">About us</a>
      <a href="#">FAQ’s</a>
    </nav>
    <a class="btn btn-login" href="#">Login</a>
    <a class="btn btn-register" href="#">Register</a>
  </header>

  <section class="hero">
    <div class="hero-visual" role="img" aria-label="Person touching floating hexagonal safety and care icons"></div>
    <h1 class="hero-title">Welcome to <strong>mytrekko.globe</strong></h1>
    <p class="hero-sub">A solution allowing smart wearables to be integrated into a safety management solution.</p>
    <div class="hero-dots"><span class="is-active"></span><span></span><span></span><span></span></div>
  </section>

  <section class="features">
    <h2 class="section-title">Features</h2>
    <h3 class="features-sub">Health care app</h3>
    <p class="features-copy">Sed ut perspiciatis unde omnis iste natus error sit voluptatem accusantium doloremque laudantium, totam rem aperiam, eaque ipsa quae ab illo inventore veritatis et quasi architec Sed ut perspiciatis unde omnis iste natus error sit voluptatem accusantium doloremque laudantium</p>
    <a class="read-more" href="#">Read more</a>
    <div class="features-visual" role="img" aria-label="Smartphone surrounded by care kit items"></div>
  </section>

  <section class="how">
    <h2 class="section-title">How it works</h2>

    <div class="step step-wear">
      <svg viewBox="0 0 52 72" width="52" aria-hidden="true">
        <rect x="9" y="0" width="34" height="10" fill="#14a99b"/>
        <rect x="9" y="62" width="34" height="10" fill="#14a99b"/>
        <rect x="2" y="10" width="46" height="52" rx="6" fill="#14a99b"/>
        <rect x="50" y="28" width="3" height="12" fill="#14a99b"/>
        <rect x="9" y="17" width="32" height="38" rx="3" fill="#fff"/>
        <path d="M14 31 L22 23 M14 38 L28 24" stroke="#14a99b" stroke-width="3" stroke-linecap="round"/>
      </svg>
      <h3 class="step-title">Wearables</h3>
      <p class="step-copy">Optional: Put your wearable to good use, we integrate to Pulsewrist Band, Stridely and others from our My Trekko Mobile app.</p>
    </div>

    <div class="step step-mobile">
      <svg viewBox="0 0 60 74" width="60" aria-hidden="true">
        <rect x="0" y="0" width="42" height="74" rx="4" fill="#14a99b"/>
        <rect x="5" y="10" width="32" height="52" fill="#fff"/>
        <circle cx="37" cy="36" r="14" fill="#14a99b"/>
        <g fill="#14a99b">
          <rect x="34" y="17" width="6" height="38" rx="1"/>
          <rect x="18" y="33" width="38" height="6" rx="1"/>
          <rect x="34" y="17" width="6" height="38" rx="1" transform="rotate(45 37 36)"/>
          <rect x="34" y="17" width="6" height="38" rx="1" transform="rotate(-45 37 36)"/>
        </g>
        <circle cx="37" cy="36" r="6" fill="#fff"/>
      </svg>
      <h3 class="step-title">My Trekko Mobile</h3>
      <p class="step-copy">Provides the smarts between you and mission control, with two way messages, panic button and a coming soon buddy system.</p>
    </div>

    <div class="step step-control">
      <svg viewBox="0 0 52 76" width="52" aria-hidden="true">
        <path d="M26 74 C18 58 3 44 3 26 A23 23 0 0 1 49 26 C49 44 34 58 26 74 Z" fill="none" stroke="#14a99b" stroke-width="3"/>
        <circle cx="26" cy="24" r="10" fill="none" stroke="#14a99b" stroke-width="3"/>
      </svg>
      <h3 class="step-title">Mission control</h3>
      <p class="step-copy">Provides centralised management and access to the User base for things like: Geo Fencing \ Alerting \ Messaging \ Response..</p>
    </div>
  </section>

  <aside class="blog">
    <h2 class="section-title">Blog post</h2>
    <div class="blog-author">
      <div class="avatar" role="img" aria-label="Author portrait"></div>
      <div>
        <div class="posted">posted by</div>
        <div class="author-name">Jhonny Doe</div>
      </div>
    </div>
    <p class="blog-copy">Neque porro quisquam est qui dolorem ipsum quia dolor sit amet, consectetur, ad velit</p>
    <a class="read-more" href="#">Read more</a>
  </aside>

  <footer class="site-footer">
    <div class="footer-links"><a href="#">About us</a><span>\</span><a href="#">FAQ’s</a><span>\</span><a href="#">T&amp;C’s</a></div>
    <p class="copyright">Copyright 2016, <a href="#">mytrekko-demo.net</a>, All Right Reserved.</p>
    <div class="social">
      <a class="s-one" href="#" aria-label="Social profile"></a>
      <a class="s-two" href="#" aria-label="Social profile"></a>
      <a class="s-three" href="#" aria-label="News feed"></a>
    </div>
  </footer>
</body>
</html>
```